web design for specialty coffee shop

We are online shop selling specialty coffeee.
Our brand concept keywords are -
specialty coffee, knowledge, discovery, professional, convenience, collaboration.
there will be five main tabs on the homepage
[home (u icon from logo)]
[coffee]
[equipment]
[gift]
[knowledge]
[about us]
For our site, we will be using the following template.
ONLY DESIGN, NO CODING necessary as our developers will do that.
http://layoutbarn.example/item/velorina-deluxe-adaptive-storefront-theme/full_screen_preview/7351620
Use the template as a base.
You do not have to do exactly the same layout.
Creative Liberty!
For the style and color palette, please look at the attached image.
Our brown logo should match nicely with the style provided in the attachment.
Thank you for taking the time to read this post.
Looking forward to working with artmingle and the amazing designers that are part of this community.
Reason: Dear designers,
I have extended the deadline to give designers who accepted to participate in this contest some more time to submit their designs. Thank you for understanding.

```html
<!DOCTYPE html>
<html lang="en">
<head>
<meta charset="utf-8">
<title>Umoja Coffee Lab — Specialty Coffee</title>
<link href="https://fonts.googleapis.com/css2?family=Roboto+Condensed:wght@400;700&family=Rye&family=Oswald:wght@500&display=swap" rel="stylesheet">
<style>
:root{
  --bar:#9f5530;
  --bar-dark:#2a0d08;
  --peach:#f7a66c;
  --accent:#f29f64;
  --hero:#2b0605;
  --cream:#e6d6c6;
  --maroon:#4a1210;
  --red:#c8191a;
  --price:#d8542a;
  --text:#6e5e55;
  --line:#d2bfae;
}
*{margin:0;padding:0;box-sizing:border-box}
html,body{width:766px;height:1200px;overflow:hidden}
body{font-family:"Roboto Condensed",Arial,sans-serif;background:var(--cream);position:relative;color:var(--maroon)}
.abs{position:absolute}
/* header */
.header{left:0;top:0;width:766px;height:109px;background:var(--bar);border-top:6px solid #3a1208}
.header .rule{left:0;top:44px;width:766px;height:3px;border-top:1px solid #c97b4c;border-bottom:1px solid #c97b4c}
.btn-dark{background:var(--bar-dark);color:#fff;font-size:8px;font-weight:700;display:flex;align-items:center;justify-content:center;gap:6px;height:22px}
.signin{left:70px;top:12px;width:47px}
.account{left:502px;top:12px;width:87px}
.cart{left:597px;top:12px;width:94px}
.caret{width:0;height:0;border-left:3px solid transparent;border-right:3px solid transparent;border-top:5px solid #b8a090}
.logo{left:296px;top:8px;width:176px;height:79px;background:var(--peach);border:2px solid #7b3518;border-radius:14px;box-shadow:0 0 0 3px var(--peach);display:flex;flex-direction:column;align-items:center;justify-content:center}
.logo .name{font-size:26px;font-weight:700;color:#3a1208;line-height:1}
.logo .sub{font-size:11px;color:#3a1208;letter-spacing:2px}
.tagline{left:296px;top:96px;width:176px;text-align:center;font-size:8px;color:#f6c9a6}
.nav{top:77px;font-size:8px;font-weight:700;color:var(--accent);display:flex}
.nav a{color:inherit;text-decoration:none;padding:0 12px;border-left:1px solid #c47a50}
.nav a:first-child{border-left:none}
.nav-left{left:76px}
.nav-active{left:78px;top:104px;width:39px;height:4px;background:var(--red)}
.nav-right{left:481px}
.search{left:565px;top:74px;width:125px;height:19px;background:linear-gradient(#eee,#d8d8d8);border:1px solid #b89}
/* hero */
.hero{left:0;top:109px;width:766px;height:368px;background:radial-gradient(ellipse at 25% 70%,#5a1410,var(--hero) 60%)}
.hero-photo{left:50px;top:110px;width:290px;height:330px;border-radius:40%;background:radial-gradient(ellipse at 50% 60%,#d9dcde 0,#9a9ea2 35%,rgba(60,20,15,0) 70%)}
.headline{left:320px;width:374px;text-align:center;font-family:"Rye",serif;color:var(--accent);line-height:1}
.h1{top:163px;font-size:35px}
.h2{top:212px;font-size:35px}
.h3{top:262px;font-size:22px}
.h4{top:291px;font-size:20px}
.h5{top:316px;font-size:22px}
.signup{left:448px;top:375px;width:120px;height:31px;background:var(--red);color:#fff;font-family:"Oswald",sans-serif;font-size:15px;display:flex;align-items:center;justify-content:center;border:1px solid #8a0f10}
.dot{top:446px;width:6px;height:6px;background:#eee}
/* tiles */
.tile{top:490px;width:191px;height:102px;overflow:hidden}
.tile .photo{position:absolute;inset:0}
.tile .label{position:absolute;left:0;top:60px;width:155px;height:33px;background:rgba(40,5,4,.92);border-radius:0 17px 17px 0;color:var(--accent);font-size:10px;font-weight:700;display:flex;align-items:center;gap:7px;padding-left:8px}
.berries{background:linear-gradient(135deg,#4d7a2a,#b8202a 45%,#2a1a20 70%,#6aa030)}
.brew{background:linear-gradient(135deg,#6a3a20,#a06a40 50%,#3a1a0e)}
/* how it works */
.band{left:0;width:766px;height:12px;background:linear-gradient(rgba(120,80,60,0),rgba(120,80,60,.15),rgba(120,80,60,0))}
.section-title{left:0;top:627px;width:766px;text-align:center;font-size:15px;color:var(--maroon)}
.step{top:670px;width:139px;height:83px;border:1px solid var(--line);text-align:center;padding-top:10px}
.step .t{font-size:11px;margin-top:6px}
.step .d{font-size:6.5px;margin-top:4px;line-height:1.5}
/* featured */
.feat-title{left:108px;top:798px;font-size:15px}
.feat-rule{left:76px;top:827px;width:614px;height:1px;background:var(--line)}
.arrow{top:803px;width:12px;height:11px;background:#f3ece4;border:1px solid #cbb;font-size:8px;color:#998;display:flex;align-items:center;justify-content:center}
.card{top:837px;width:141px;height:133px;background:#fff;border:1px solid #ddd;display:flex;align-items:center;justify-content:center}
.bag{width:52px;height:110px;border-radius:3px}
.bag.white{background:linear-gradient(90deg,#e8e8e8,#fff,#ddd)}
.bag.kraft{background:linear-gradient(90deg,#7a5a34,#b08a5a,#6a4a28)}
.bag.black{background:linear-gradient(90deg,#1a1a1a,#3a3a3a,#111)}
.prod{width:141px}
.prod .n{font-size:7.5px;color:var(--price);position:absolute;top:142px}
.prod .d{font-size:7.5px;color:var(--text);line-height:1.6;position:absolute;top:161px}
.prod .p{font-size:15px;color:var(--price);position:absolute;top:190px;left:5px}
.prod .b{position:absolute;top:189px;left:74px;width:67px;height:19px;background:#200807;color:#fff;font-size:8px;font-weight:700;display:flex;align-items:center;padding-left:5px;clip-path:polygon(0 0,100% 0,88% 50%,100% 100%,0 100%)}
/* press */
.press{top:1084px;color:#8a8480;font-weight:700}
.badge{left:99px;top:1081px;width:56px;height:53px;border-radius:50%;background:#8a8480}
/* footer */
.footer{left:0;top:1148px;width:766px;height:52px;background:var(--hero)}
.copy{left:71px;top:1174px;font-size:7.5px;color:#e8d8d0}
.social{top:1168px;width:20px;height:20px;border-radius:50%;background:#fff}
</style>
</head>
<body>
<header class="header abs">
  <div class="rule abs"></div>
  <div class="btn-dark signin abs">SIGN IN</div>
  <div class="btn-dark account abs">MY ACCOUNT <span class="caret"></span></div>
  <div class="btn-dark cart abs">
    <svg width="11" height="9" viewBox="0 0 11 9"><path d="M0 1h2l2 5h6l1-4H3" fill="none" stroke="#ccc"/><circle cx="5" cy="8" r="1" fill="#ccc"/><circle cx="9" cy="8" r="1" fill="#ccc"/></svg>
    MY CART: (0) <span class="caret"></span></div>
  <div class="logo abs"><span class="name">umoja</span><span class="sub">coffee lab</span></div>
  <div class="tagline abs">SOPHISTICATED TASTING*</div>
  <nav class="nav nav-left abs"><a>SHOP</a><a>SUBSCRIPTION</a><a>GIFT</a><a>FAQ</a></nav>
  <nav class="nav nav-right abs"><a>KNOWLEDGE</a></nav>
  <div class="search abs"><svg class="abs" style="right:6px;top:4px" width="8" height="8" viewBox="0 0 8 8"><circle cx="3" cy="3" r="2" fill="none" stroke="#333"/><path d="M4.5 4.5L7 7" stroke="#333"/></svg></div>
</header>
<div class="nav-active abs"></div>

<section class="hero abs"></section>
<div class="hero-photo abs" role="img" aria-label="Steaming cup of black coffee on a white saucer with a few roasted beans"></div>
<div class="headline h1 abs">THE WORLD'S BEST</div>
<div class="headline h2 abs">COFFEE,</div>
<div class="headline h3 abs">EXPERTLY CHOSEN</div>
<div class="headline h4 abs">&amp;</div>
<div class="headline h5 abs">DELIVERED TO YOUR DOORSTEP.</div>
<div class="signup abs">SIGN UP NOW!</div>
<div class="dot abs" style="left:654px"></div><div class="dot abs" style="left:668px"></div><div class="dot abs" style="left:682px"></div>

<div class="tile abs" style="left:76px"><div class="photo berries" role="img" aria-label="Ripe coffee cherries on the branch"></div>
  <div class="label"><svg width="16" height="16" viewBox="0 0 16 16" fill="none" stroke="#f29f64" stroke-width="1.3"><ellipse cx="6" cy="5" rx="5" ry="3.5" transform="rotate(-30 6 5)"/><ellipse cx="10" cy="11" rx="5" ry="3.5" transform="rotate(-30 10 11)"/></svg>ABOUT UMOJA COFFEE</div></div>
<div class="tile abs" style="left:287px"><div class="photo brew" role="img" aria-label="French press beside a sack of roasted coffee beans"></div>
  <div class="label"><svg width="14" height="16" viewBox="0 0 14 16" fill="#f29f64"><path d="M5 0h4v6l5 9H0l5-9z"/></svg>HOW TO BREWING GUIDES</div></div>
<div class="tile abs" style="left:497px"><div class="photo berries" role="img" aria-label="Ripe coffee cherries on the branch"></div>
  <div class="label"><svg width="14" height="14"><rect width="14" height="14" fill="#f29f64"/></svg>UMOJA SUBSCRIPTION</div></div>

<div class="band abs" style="top:610px"></div>
<div class="section-title abs">HOW IT WORKS</div>
<div class="step abs" style="left:77px"><svg width="20" height="20"><rect width="20" height="20" fill="#3a0d0a"/></svg><div class="t">SUBSRIBE TO UMOJA</div><div class="d">RECEIVE A UMOJA TASTER'S BOX<br>EVERY MONTH</div></div>
<div class="step abs" style="left:234px"><svg width="22" height="20" viewBox="0 0 16 16" fill="none" stroke="#3a0d0a" stroke-width="1.5"><ellipse cx="6" cy="5" rx="5" ry="3.5" transform="rotate(-30 6 5)"/><ellipse cx="10" cy="11" rx="5" ry="3.5" transform="rotate(-30 10 11)"/></svg><div class="t">PREMIUM BEANS</div><div class="d">PREMIUM BEANS FROM TOP UMOJA<br>COFFEE LAP</div></div>
<div class="step abs" style="left:391px"><svg width="18" height="20" viewBox="0 0 14 16" fill="#3a0d0a"><path d="M5 0h4v6l5 9H0l5-9z"/></svg><div class="t">CURATED</div><div class="d">BLIND TASTE-TESTED BY INDUSTRY<br>EXPERTS</div></div>
<div class="step abs" style="left:549px"><svg width="26" height="20" viewBox="0 0 26 20" fill="#3a0d0a"><rect x="6" y="2" width="18" height="16" rx="3"/><path d="M7 6H3v8h4" fill="none" stroke="#3a0d0a" stroke-width="2.5"/></svg><div class="t">DELIVERED</div><div class="d">FRESHLY ROASTED AND SENT<br>MONTHLY</div></div>
<div class="band abs" style="top:766px"></div>

<svg class="abs" style="left:77px;top:798px" width="24" height="18" viewBox="0 0 26 20" fill="#200807"><rect x="6" y="1" width="19" height="18" rx="3"/><path d="M7 6H3v8h4" fill="none" stroke="#200807" stroke-width="2.5"/></svg>
<div class="feat-title abs">UMOJA COFFEE FEATURED IN APRIL</div>
<div class="arrow abs" style="left:663px">&lsaquo;</div><div class="arrow abs" style="left:677px">&rsaquo;</div>
<div class="feat-rule abs"></div>

<div class="card abs" style="left:76px"><div class="bag white" role="img" aria-label="White bag of decaf coffee"></div></div>
<div class="card abs" style="left:233px"><div class="bag kraft" role="img" aria-label="Kraft paper bag of espresso beans"></div></div>
<div class="card abs" style="left:390px"><div class="bag black" role="img" aria-label="Black bag of roasted coffee"></div></div>
<div class="card abs" style="left:549px"><div class="bag black" role="img" aria-label="Black bag of roasted coffee"></div></div>

<div class="prod abs" style="left:76px;top:837px"><div class="n">LARCH LANE :: VISTA ROJA DECAF</div><div class="d">German chocolate, toffee, French vanilla<br>bean, buttery finish</div><div class="p">$15.00</div><div class="b">ADD TO CART</div></div>
<div class="prod abs" style="left:233px;top:837px"><div class="n">LARCH LANE :: VISTA ROJA DECAF</div><div class="d">German chocolate, toffee, French vanilla<br>bean, buttery finish</div><div class="p">$15.00</div><div class="b">ADD TO CART</div></div>
<div class="prod abs" style="left:390px;top:837px"><div class="n">LARCH LANE :: VISTA ROJA DECAF</div><div class="d">German chocolate, toffee, French vanilla<br>bean, buttery finish</div><div class="p">$15.00</div><div class="b">ADD TO CART</div></div>
<div class="prod abs" style="left:549px;top:837px"><div class="n">LARCH LANE :: VISTA ROJA DECAF</div><div class="d">German chocolate, toffee, French vanilla<br>bean, buttery finish</div><div class="p">$15.00</div><div class="b">ADD TO CART</div></div>

<div class="band abs" style="top:1062px"></div>
<div class="badge abs"></div>
<div class="press abs" style="left:180px;top:1090px;font-size:24px">PALATE POST</div>
<div class="press abs" style="left:367px;top:1091px;font-size:23px;font-weight:400">ByteWire</div>
<div class="press abs" style="left:508px;top:1078px;font-size:40px">dailyhack</div>

<footer class="footer abs"></footer>
<div class="copy abs">© 2013 Umoja Coffee Lab. All Rights Reserved.</div>
<div class="social abs" style="left:573px"></div>
<div class="social abs" style="left:596px"></div>
<div class="social abs" style="left:619px"></div>
<div class="social abs" style="left:642px"></div>
<div class="social abs" style="left:665px"></div>
</body>
</html>
```